Business Card Design

as above
one side to be name of business and information about business inside an imessage text bubble.
other side to be contact details around an email icon . 'envelope'

Target Market(s)

seniors

Industry/Entity Type

Business

Contact Information for Business Card

Tech Along-Keep Along
Marlene Hobb
0461 837 204
Marlene.techalong@quillmail.test
ABN:74618250913

Technology help for seniors in your own home.- tablets, e-readers, mobile phones, internet, email, computers. No question too small.

```html
<!DOCTYPE html>
<html lang="en">
<head>
<meta charset="utf-8">
<title>Tech Along-Keep Along – Business Card</title>
<link rel="stylesheet" href="https://fonts.googleapis.com/css2?family=Cabin:ital,wght@0,400;0,700;1,700&display=swap">
<style>
  :root {
    --paper: #ffffff;
    --bubble: #f0aa58;
    --panel: #22a36b;
    --brand-ink: #7a1406;
    --ink: #1c2326;
    --name-orange: #f0aa58;
    --contact-white: #ffffff;
    --icon-stroke: #111111;
    --icon-light: #ffffff;
    --icon-tint: #cfeeee;
  }
  html, body {
    margin: 0;
    padding: 0;
    overflow: hidden;
    background: var(--paper);
  }
  .card {
    display: block;
    width: 1200px;
    height: 741px;
  }
  .card__background { fill: var(--paper); }
  .bubble { fill: var(--bubble); }
  .contact-panel { fill: var(--panel); }

  .brand {
    font-family: "Cabin", sans-serif;
    font-weight: 700;
    font-size: 56px;
    fill: var(--brand-ink);
  }

  .services {
    font-family: "Cabin", sans-serif;
    font-weight: 400;
    font-size: 38px;
    fill: var(--ink);
  }
  .tagline {
    font-family: "Cabin", sans-serif;
    font-weight: 700;
    font-size: 40px;
    fill: var(--ink);
  }

  .contact {
    font-family: "Cabin", sans-serif;
    fill: var(--contact-white);
  }
  .contact__name {
    font-weight: 700;
    font-style: italic;
    font-size: 46px;
    fill: var(--name-orange);
  }
  .contact__phone {
    font-weight: 700;
    font-size: 52px;
  }
  .contact__email {
    font-weight: 400;
    font-size: 34px;
  }
  .contact__abn {
    font-weight: 400;
    font-size: 33px;
  }

  .envelope__body {
    fill: url(#envelope-shade);
    stroke: var(--icon-stroke);
    stroke-width: 5;
    stroke-linejoin: round;
  }
  .envelope__fold {
    fill: none;
    stroke: var(--icon-stroke);
    stroke-width: 4;
    stroke-linejoin: round;
    stroke-linecap: round;
  }
</style>
</head>
<body>
<svg class="card" viewBox="0 0 1200 741" xmlns="http://www.w3.org/2000/svg" role="img" aria-label="Tech Along-Keep Along business card">
  <defs>
    <linearGradient id="envelope-shade" x1="0" y1="0" x2="1" y2="0">
      <stop offset="0" stop-color="#ffffff"/>
      <stop offset="1" stop-color="#cfeeee"/>
    </linearGradient>
  </defs>

  <rect class="card__background" x="0" y="0" width="1200" height="741"/>

  <!-- Message bubble -->
  <g class="message">
    <ellipse class="bubble" cx="440" cy="314" rx="384" ry="271"/>
    <path class="bubble" d="M322 560 C318 610 300 660 279 697 C340 672 410 628 462 566 Z"/>

    <text class="brand" x="440" y="262" text-anchor="middle">Tech Along-Keep Along</text>

    <text class="services" text-anchor="middle">
      <tspan x="443" y="392">Technology help for seniors in</tspan>
      <tspan x="443" y="433">your own home.- tablets, e-readers,</tspan>
      <tspan x="443" y="474">mobile phones, internet,</tspan>
      <tspan x="443" y="515">email, computers.</tspan>
    </text>

    <text class="tagline" x="176" y="632">No question too small.</text>
  </g>

  <!-- Contact panel -->
  <g class="contact-side">
    <rect class="contact-panel" x="860" y="0" width="340" height="741"/>

    <text class="contact contact__name" x="956" y="428" transform="rotate(-90 956 428)" textLength="318" lengthAdjust="spacingAndGlyphs">Marlene Hobb</text>
    <text class="contact contact__phone" x="1021" y="443" transform="rotate(-90 1021 443)" textLength="340" lengthAdjust="spacingAndGlyphs">0461 837 204</text>
    <text class="contact contact__email" x="1084" y="644" transform="rotate(-90 1084 644)" textLength="552" lengthAdjust="spacingAndGlyphs">Marlene.techalong@quillmail.test</text>
    <text class="contact contact__abn" x="1128" y="524" transform="rotate(-90 1128 524)" textLength="314" lengthAdjust="spacingAndGlyphs">ABN:74618250913</text>

    <g class="envelope" aria-hidden="true">
      <rect class="envelope__body" x="923" y="480" width="100" height="156" rx="3"/>
      <path class="envelope__fold" d="M925 483 L968 540 C986 548 986 570 968 578 L925 633"/>
      <path class="envelope__fold" d="M1021 483 L990 530 M1021 633 L990 590"/>
    </g>
  </g>
</svg>
</body>
</html>
```